Single page Web Application UI Design - Kendo UI / Angular2

We are in need of an application UI Design for a single web application page. We currently have a web based .net application that we are upgrading using Kendo UI and Angular. We have completed the wire frame and some of the functionality but we are now in need of a designer to provide an upgraded look/feel to the page.
The project will be two phases, with possible future ongoing hourly work depending on results.
Phase 1:
Take the current provided application page and create a design update for the panels, buttons, colors, etc. The output should be an HTML page. The underlying application code will use Kendo UI controls on Angular.
Phase 2:
Once we have decided on a final design we will need 10 color/skin variations designed. We will take the 10 skins and code them into css layers in Kendo for user selected skin changes. The output of this phase will be 10 HTML pages with images/colors to support the css layers development.
Access/login information:
1. Please open a browser to the following link:
http://203.118.77.42/LedgerProbe_VTrial
2. Login with the following credentials:
Login: Design
Pass: Maple7
3. Once logged in paste the following URL link into your browser:
http://203.118.77.42/LedgerProbe_vTrial/FreshWave/ReviewItem/518406/QP7ZD314KM8Rt
Any questions, concerns, or suggestions please contact us directly at: support@quillvantor.com
Thank you,
Colin
Healthcare claim auditors
1 page

```html
<!DOCTYPE html>
<html lang="en">
<head>
<meta charset="utf-8">
<title>LedgerProbe – Audit Claim</title>
<link href="https://fonts.googleapis.com/css2?family=Roboto:wght@300;400;500;700&display=swap" rel="stylesheet">
<style>
:root{
  --green:#7dc22b;
  --dark:#231f20;
  --grid-head:#5b5b5b;
  --grid-filter:#707070;
  --page:#efefef;
  --line:#d6d6d6;
  --text:#222;
  --muted:#555;
  --white:#fff;
}
*{box-sizing:border-box;margin:0;padding:0}
html,body{width:1200px;height:1081px;overflow:hidden;background:var(--page)}
body{font-family:'Roboto',Arial,sans-serif;color:var(--text)}
.stage{position:absolute;left:0;top:0;width:1366px;height:1230px;transform:scale(.87848);transform-origin:0 0;background:var(--page)}
.abs{position:absolute}

/* header */
.topbar{left:0;top:0;width:1366px;height:100px;background:var(--white)}
.brand{left:16px;top:24px}
.brand-name{font-size:40px;font-weight:400;color:#333;letter-spacing:-.5px;display:flex;align-items:center;gap:10px}
.brand-mark{width:14px;height:14px;background:var(--green);display:inline-block}
.brand-tag{font-size:14px;color:#666;font-weight:300;margin-left:108px;margin-top:-2px}
.field{top:26px;height:50px;border:1px solid #bbb;display:flex;align-items:center;padding-left:16px;font-size:14px;gap:14px}
.info-strip{left:781px;top:26px;width:569px;height:50px;border:1px solid #bbb;display:flex}
.info-strip div{flex:1;border-right:1px solid #bbb;padding:7px 0 0 14px;font-size:12px;color:#555}
.info-strip div:last-child{border-right:0}
.info-strip b{display:block;font-size:14px;font-weight:400;color:#222;margin-top:2px}

.mainnav{left:0;top:101px;width:1366px;height:39px;display:flex;background:var(--white);border-bottom:1px solid var(--line)}
.mainnav a{display:flex;align-items:center;justify-content:center;font-size:11px;font-weight:700;letter-spacing:3px;color:#333;text-decoration:none;border-right:1px solid var(--line)}
.mainnav a.active{background:var(--green);color:#fff}

/* toolbar */
.toolbar{left:22px;top:168px;width:1323px;height:42px;background:var(--white);border:1px solid var(--line);display:flex;align-items:center}
.toolbar .tab{height:42px;background:var(--dark);color:#fff;font-size:13px;display:flex;align-items:center;padding:0 20px;border-right:1px solid #444;margin-top:-1px}
.status{margin-left:auto;display:flex;font-size:13px;color:#444;padding-right:14px}
.status span{padding:0 16px;border-left:1px solid #ccc}
.status span:first-child{border-left:0}
.status b{color:var(--green);font-weight:700;font-size:14px}

/* claim details */
.details{left:22px;top:234px;width:1323px;height:268px;background:var(--white);border:1px solid var(--line);display:flex}
.dcol{border-right:1px solid var(--line);padding-top:12px}
.dcol:last-child{border-right:0}
.dhead{font-size:12px;font-weight:500;padding:0 0 10px 20px;border-bottom:1px solid var(--line);display:flex;align-items:center;gap:8px;margin-bottom:8px}
.icon-i{width:12px;height:12px;border-radius:50%;background:#222;color:#fff;font-size:9px;font-weight:700;display:inline-flex;align-items:center;justify-content:center;font-style:normal}
.kv{display:grid;font-size:11px;row-gap:0}
.kv div{height:25.6px;display:flex;align-items:center}
.kv .v{font-weight:500}

/* left panel */
.leftpanel{left:22px;top:527px;width:568px;height:537px;background:var(--white);border:1px solid var(--line)}
.ltabs{height:41px;background:var(--dark);display:flex}
.ltabs a{color:#fff;font-size:13px;display:flex;align-items:center;padding:0 17px;text-decoration:none}
.ltabs a.active{background:var(--green);padding:0 12px}
.note{font-size:12px;display:flex;align-items:center;gap:8px}
.btn{width:142px;height:42px;background:var(--green);color:#fff;font-size:14px;font-weight:500;display:flex;align-items:center;justify-content:center}
.radio{width:24px;height:24px;border:1px solid #bbb;border-radius:50%;display:inline-flex;align-items:center;justify-content:center}
.radio.on::after{content:"";width:14px;height:14px;border-radius:50%;background:var(--green)}
.others{left:320px;top:625px;width:245px;height:163px;border:1px solid #ccc}
.others .h{height:39px;background:#f2f2f2;border-bottom:1px solid #ccc;font-size:11px;display:flex;align-items:center;padding-left:12px}
.others .r{height:34px;border-bottom:1px solid #ddd}
.pager-mini{display:flex;align-items:center;padding:10px 13px;font-size:10px}
.pager-mini i{width:22px;height:22px;border:1px solid #ccc;display:inline-flex;align-items:center;justify-content:center;font-style:normal;font-size:7px;color:#3a7bd5}
.pager-mini i.cur{background:#3a7bd5;color:#fff;font-size:10px}

/* history grid */
.history{left:610px;top:527px;width:735px;height:537px;background:var(--white);border:1px solid var(--line)}
.hhead{height:42px;background:var(--dark);color:#fff;display:flex;align-items:center;padding-left:14px;gap:10px;font-size:14px}
.export{margin-left:auto;margin-right:8px;background:var(--green);height:28px;padding:0 10px;display:flex;align-items:center;gap:8px;font-size:14px}
.export .sq{width:14px;height:14px;border:2px solid #fff}
.grid{display:grid;grid-template-columns:180px 182px 190px 183px}
.gh{height:34px;background:var(--grid-head);color:#fff;font-size:11px;display:flex;align-items:center;justify-content:space-between;padding:0 12px;border-right:1px solid #888}
.gf{height:42px;background:var(--grid-filter);display:flex;align-items:center;gap:4px;padding:0 6px 0 8px;border-right:1px solid #888}
.gf .in{flex:1;height:28px;background:#fff;display:flex;align-items:center;justify-content:flex-end;padding-right:8px}
.gf .fb{width:30px;height:28px;background:#fff;display:flex;align-items:center;justify-content:center}
.gc{font-size:11px;line-height:19px;padding:14px 14px 0;border-right:1px solid #ccc;color:#222}
.gc.alt{background:#f4f4f4}
.gpager{position:absolute;left:14px;right:14px;bottom:10px;display:flex;align-items:center;gap:8px;font-size:10px}
.gpager i{width:19px;height:19px;border:1px solid #bbb;display:inline-flex;align-items:center;justify-content:center;font-style:normal}
.gpager i.g{background:var(--green);border-color:var(--green)}

/* footer */
.footer{left:0;top:1092px;width:1366px;height:138px;background:var(--dark)}
.theme{left:153px;top:35px;width:209px;height:34px;background:#f2f2f2;display:flex;align-items:center;gap:14px;padding-left:14px;font-size:12px}
.fbtns{left:387px;top:35px;display:flex;gap:12px}
.fbtns a{height:34px;background:var(--green);color:#fff;font-size:12px;font-weight:700;letter-spacing:2.6px;display:flex;align-items:center;padding:0 18px;text-decoration:none}
.copy{left:0;width:1366px;top:92px;text-align:center;color:#ddd;font-size:11px;padding-right:0;margin-left:-50px}
</style>
</head>
<body>
<div class="stage">

  <header class="abs topbar">
    <div class="abs brand">
      <div class="brand-name">ledgerprobe <span class="brand-mark"></span></div>
      <div class="brand-tag">Manage Payment Integrity</div>
    </div>
    <div class="abs field" style="left:337px;width:209px">
      <svg width="12" height="8" viewBox="0 0 12 8"><path d="M1 1l5 5 5-5" fill="none" stroke="#222" stroke-width="1.6"/></svg>Application
    </div>
    <div class="abs field" style="left:557px;width:209px">
      <svg width="12" height="12" viewBox="0 0 12 12"><circle cx="5" cy="5" r="3.8" fill="none" stroke="#222" stroke-width="1.5"/><path d="M8 8l3 3" stroke="#222" stroke-width="1.6"/></svg>Claim No.
    </div>
    <div class="abs info-strip">
      <div>Customer<b>FreshWave Demo</b></div>
      <div>Welcome<b>Demo Test</b></div>
      <div>User Account Role<b>Admin</b></div>
      <div>Current user account<b>Admin</b></div>
    </div>
  </header>

  <nav class="abs mainnav">
    <a class="active" style="width:238px">HOME</a>
    <a style="width:283px">SAMPLE</a>
    <a style="width:337px">ERROR</a>
    <a style="width:272px">FLAG</a>
    <a style="width:236px;border-right:0">ADMIN</a>
  </nav>

  <div class="abs toolbar">
    <div class="tab">Audit Claim</div>
    <div class="tab">Log New Error</div>
    <div class="tab">Errors on Claim</div>
    <div class="status">
      <span>Sample id : <b>3850</b></span>
      <span>Claim No. : <b>XYHAHFKGs</b></span>
      <span>Claim Status. : <b>Reviewed</b></span>
      <span>Process Status. : <b>Pending</b></span>
      <span>No.of Errors. : <b>5</b></span>
    </div>
  </div>

  <section class="abs details">
    <div class="dcol" style="width:380px">
      <div class="dhead"><i class="icon-i">i</i>Claim Details</div>
      <div class="kv" style="grid-template-columns:110px 22px 1fr;padding-left:22px">
        <div>Sample Name</div><div>:</div><div class="v">OPS : Jul 20 2015 - Jil 26 2015</div>
        <div>Claim Source</div><div>:</div><div class="v">Topaz / Corvell Finalized Claim Data</div>
        <div>Strata ID</div><div>:</div><div class="v">1</div>
        <div>Date Sampled</div><div>:</div><div class="v">07/25/2015</div>
        <div>Sampled Days Old</div><div>:</div><div class="v">438</div>
        <div>Allocated To</div><div>:</div><div class="v">MARCUS ELLERY</div>
        <div>Allocated Date</div><div>:</div><div class="v">07/27/2015</div>
        <div>Allocated Days old</div><div>:</div><div class="v">436</div>
      </div>
    </div>
    <div class="dcol" style="width:279px;padding-top:35px">
      <div class="kv" style="grid-template-columns:110px 22px 1fr;padding-left:37px">
        <div>Claim No.</div><div>:</div><div class="v">YFHGKSHGs</div>
        <div>Claim Type</div><div>:</div><div class="v">Payable</div>
        <div>No. of Lines</div><div>:</div><div class="v">1</div>
        <div>Last Touch User</div><div>:</div><div class="v">CS5682</div>
        <div>Paid Amount</div><div>:</div><div class="v">$5.75</div>
        <div>Billed Amount</div><div>:</div><div class="v">$5.75</div>
        <div>Allowed Amount</div><div>:</div><div class="v">$5.75</div>
        <div>Denied Amount</div><div>:</div><div class="v">$5.75</div>
      </div>
    </div>
    <div class="dcol" style="width:294px;padding-top:37px">
      <div class="kv" style="grid-template-columns:125px 27px 1fr;padding-left:39px">
        <div>Post Date</div><div>:</div><div class="v">07/20/2015</div>
        <div>Received Date</div><div>:</div><div class="v">07/20/2015</div>
        <div>Date of Service Start</div><div>:</div><div class="v">07/20/2015</div>
        <div>Date of service end</div><div>:</div><div class="v">07/20/2015</div>
        <div>Is original</div><div>:</div><div class="v">Original</div>
        <div>Form Type</div><div>:</div><div class="v">HCFA</div>
        <div>Has Denied Lines</div><div>:</div><div class="v">No</div>
        <div>Clerical Field count</div><div>:</div><div class="v">19</div>
      </div>
    </div>
    <div class="dcol" style="width:370px;padding-top:37px">
      <div class="kv" style="grid-template-columns:127px 22px 1fr;padding-left:36px">
        <div>Provider Name</div><div>:</div><div class="v">FELIX ARDENT MD PROVIDER</div>
        <div>Provider No.</div><div>:</div><div class="v">4225</div>
        <div>Provider TaxID</div><div>:</div><div class="v">9365 4565</div>
        <div>Employer Group Name</div><div>:</div><div class="v">ACA ADULT 55-64 MULT</div>
        <div>Group No.</div><div>:</div><div class="v">26156</div>
        <div>Line of Busniess</div><div>:</div><div class="v">SUP</div>
        <div>Line of Business ID</div><div>:</div><div class="v">10</div>
        <div>Prepostpay</div><div>:</div><div class="v">Posted</div>
      </div>
    </div>
  </section>

  <section class="abs leftpanel">
    <div class="ltabs">
      <a class="active">Audit Claim</a><a>Review Checklist</a><a>Add Note</a><a>Assign 2nd Auditor</a><a>Line Details</a>
    </div>
    <div class="abs note" style="left:24px;top:66px"><i class="icon-i">i</i>Manage Claim Audit Status:(reviewed)</div>
    <div class="abs btn" style="left:26px;top:106px">ReOpen Claim</div>
    <div class="abs btn" style="left:26px;top:165px">Reviewed</div>
    <div class="abs btn" style="left:26px;top:226px">Pended</div>
    <div class="abs btn" style="left:26px;top:285px">Pend For ReAduit</div>
    <i class="abs icon-i" style="left:186px;top:301px">i</i>
    <div class="abs" style="left:28px;top:355px;font-size:12px">Did you receive &nbsp;this claim completely</div>
    <div class="abs" style="left:28px;top:379px;display:flex;align-items:center;gap:10px;font-size:13px">
      <span class="radio on"></span>No<span class="radio" style="margin-left:22px"></span>Yes
    </div>
    <div class="abs btn" style="left:26px;top:447px">Close Claim</div>
    <div class="abs" style="left:298px;top:67px;font-size:14px">Other Audtis of this Claim</div>
    <div class="abs others" style="left:298px;top:98px">
      <div class="h">Sample ID / &nbsp;Sample Name</div>
      <div class="r"></div><div class="r"></div>
      <div class="pager-mini"><i>|◀</i><i>◀</i><i class="cur">0</i><i>▶</i><i>▶|</i><span style="margin-left:18px">No items to display</span></div>
    </div>
  </section>

  <section class="abs history">
    <div class="hhead"><i class="icon-i" style="width:15px;height:15px;font-size:10px;background:#fff;color:#222">i</i>Audit History Component
      <div class="export"><span class="sq"></span>Export to Excel</div>
    </div>
    <div class="grid">
      <div class="gh">Activity <span>⌄</span></div>
      <div class="gh">DateLog <span>⌄</span></div>
      <div class="gh">By <span>⌄</span></div>
      <div class="gh" style="border-right:0">DetailNote <span>⌄</span></div>
      <div class="gf"><span class="in"><svg width="11" height="11"><rect x=".5" y="1.5" width="10" height="9" fill="none" stroke="#999"/><path d="M1 4h9" stroke="#999"/></svg></span><span class="fb"><svg width="12" height="12"><path d="M0 1h12L7 6v6L5 11V6z" fill="#555"/></svg></span></div>
      <div class="gf"><span class="in"><svg width="11" height="11"><rect x=".5" y="1.5" width="10" height="9" fill="none" stroke="#999"/><path d="M1 4h9" stroke="#999"/></svg></span><span class="fb"><svg width="12" height="12"><path d="M0 1h12L7 6v6L5 11V6z" fill="#555"/></svg></span></div>
      <div class="gf"><span class="in"><svg width="11" height="11"><rect x=".5" y="1.5" width="10" height="9" fill="none" stroke="#999"/><path d="M1 4h9" stroke="#999"/></svg></span><span class="fb"><svg width="12" height="12"><path d="M0 1h12L7 6v6L5 11V6z" fill="#555"/></svg></span></div>
      <div class="gf" style="border-right:0"><span class="in"><svg width="11" height="11"><rect x=".5" y="1.5" width="10" height="9" fill="none" stroke="#999"/><path d="M1 4h9" stroke="#999"/></svg></span><span class="fb"><svg width="12" height="12"><path d="M0 1h12L7 6v6L5 11V6z" fill="#555"/></svg></span></div>

      <div class="gc" style="height:70px">New Error Logged<br>(Error Id : 9154)</div>
      <div class="gc" style="padding-top:21px">2016-09-15T2:34:13</div>
      <div class="gc" style="padding-top:21px">Harold Penwick</div>
      <div class="gc" style="border-right:0">Create New Eroor (Id: 9154)<br>dd added as a primary note:</div>

      <div class="gc alt" style="height:58px;padding-top:8px">New Error Assignes to<br>Supervisor ( Error ID : 9154)</div>
      <div class="gc alt" style="padding-top:15px">2016-09-15T2:34:13</div>
      <div class="gc alt" style="padding-top:15px">Harold Penwick</div>
      <div class="gc alt" style="border-right:0;padding-top:8px">Create New Eroor (Id: 9154)<br>dd added as a primary note:</div>

      <div class="gc" style="height:72px;padding-top:12px">New Error Logged<br>(Error Id : 9154)</div>
      <div class="gc" style="padding-top:19px">2016-09-15T2:34:13</div>
      <div class="gc" style="padding-top:19px">Harold Penwick</div>
      <div class="gc" style="border-right:0;padding-top:12px">Create New Eroor (Id: 9154)<br>dd added as a primary note:</div>

      <div class="gc alt" style="height:98px;padding-top:8px">New Error Assignes to<br>Supervisor ( Error ID : 9154)</div>
      <div class="gc alt" style="padding-top:15px">2016-09-15T2:34:13</div>
      <div class="gc alt" style="padding-top:15px">Harold Penwick</div>
      <div class="gc alt" style="border-right:0;padding-top:6px">New Error Description:<br>Test Processor Error #1 Ray<br>Ray took the wrong Deductible<br>and this needs to be fixed</div>

      <div class="gc" style="height:79px;padding-top:16px">New Error Logged<br>(Error Id : 9154)</div>
      <div class="gc" style="padding-top:23px">2016-09-15T2:34:13</div>
      <div class="gc" style="padding-top:23px">Harold Penwick</div>
      <div class="gc" style="border-right:0;padding-top:16px">Create New Eroor (Id: 9154)<br>dd added as a primary note:</div>
    </div>
    <div class="gpager">
      <i class="g"><svg width="7" height="8"><path d="M6 0v8L0 4z" fill="#fff"/></svg></i>
      <i>1</i><i>2</i><i>3</i><i>4</i>
      <i class="g"><svg width="7" height="8"><path d="M1 0v8l6-4z" fill="#fff"/></svg></i>
      <span style="margin-left:auto;font-size:11px">1 - 5 &nbsp;of 17 items</span>
    </div>
  </section>

  <footer class="abs footer">
    <div class="abs theme"><svg width="12" height="8" viewBox="0 0 12 8"><path d="M1 1l5 5 5-5" fill="none" stroke="#222" stroke-width="1.6"/></svg>Select Theme</div>
    <div class="abs fbtns">
      <a>NEED HELP</a><a>REPORT BUG</a><a>SUGGEST ENHANCEMENT</a><a>USER TRAINING</a><a>SAMPLE REQUEST</a>
    </div>
    <div class="abs copy">LedgerProbe TM v04.42.200 Copyright @ 1999-216 Quillvantor inc, all right reserved</div>
  </footer>

</div>
</body>
</html>
```